Poster to display corporate values and behaviors associated

I'm looking for a graphic design, probably in the form of a poster or something that can be posted on walls throughout the building that identifies our "Brightwell Values".
The values are: Accountability, Honesty, Excellence, Teamwork, and Family.
Associated behaviors (which I'd like displayed with each value) are:
Accountability: Integrity, Trust, Self-Discipline, Tranparency
Honesty: Integrity, Pschological Safety, Vulnerability, Dependable, Ethical, Truthful
Excellence: Consistent Quality, Continuous Improvement, Attention to Detail, Accepting Challenges, Service to others (internally and externally)
Teamwork: Acknowledging strengths and weaknesses, Compromise, Active listening, Punctuality, Open to Feedback, Mutual Respect
Family: Acceptance, Compassion, Being there for each other, Celebrating Successes
I have attached an example that my team put together, however it is too small for something on the wall, and am looking for other options.
Feel free to use our corporate logo as well (attached)

```html
<!DOCTYPE html>
<html lang="en">
<head>
<meta charset="utf-8">
<title>Brightwell Values</title>
<link rel="stylesheet" href="https://fonts.googleapis.com/css2?family=Montserrat:ital,wght@0,500;0,700;0,800;1,700&display=swap">
<style>
  :root {
    --sky: #d8eef9;
    --sky-deep: #c9e6f6;
    --card: #f2f9fd;
    --ink: #111111;
    --brand-red: #ec1c24;
    --teamwork: #0b76bd;
    --honesty: #6d2b8b;
    --accountability: #f37021;
    --excellence: #1a9f6c;
    --family: #c72160;
    --white: #ffffff;
  }
  * { box-sizing: border-box; margin: 0; padding: 0; }
  html, body { width: 800px; height: 1200px; overflow: hidden; }
  body { font-family: "Montserrat", Arial, sans-serif; color: var(--ink); }
  .poster {
    position: relative; width: 800px; height: 1200px; overflow: hidden;
    background: linear-gradient(180deg, var(--sky) 0%, var(--sky-deep) 55%, var(--sky) 100%);
  }
  .brand {
    position: absolute; left: 0; width: 800px; top: 52px; text-align: center;
  }
  .brand-name { font-weight: 800; font-size: 38px; letter-spacing: 7px; line-height: 1; color: var(--ink); }
  .brand-tagline { margin-top: 10px; font-weight: 800; font-size: 16px; letter-spacing: 4.5px; color: var(--brand-red); }
  .title {
    position: absolute; left: 0; width: 800px; top: 132px; text-align: center;
    font-weight: 800; font-size: 82px; letter-spacing: 1px; color: var(--brand-red); line-height: 1;
  }
  .presenter {
    position: absolute; left: 318px; top: 250px; width: 425px; height: 690px;
    border-radius: 200px 200px 20px 20px;
    background: linear-gradient(180deg, #3b1c12 0%, #e8a567 28%, #f37421 48%, #1b1a3d 75%, #1b1a3d 100%);
    opacity: .85;
  }
  .value { position: absolute; }
  .value-card {
    position: absolute; background: var(--card); border-radius: 0 0 14px 14px;
    padding: 12px 14px 0 17px; font-weight: 500; font-size: 15.6px; line-height: 20.2px;
  }
  .value-band {
    position: absolute; height: 35px; border-radius: 0 4px 0 0;
    color: var(--white); font-weight: 800; font-size: 22.5px; letter-spacing: 1.5px;
    padding-left: 14px; line-height: 35px; white-space: nowrap;
  }
  .value-badge {
    position: absolute; width: 70px; height: 70px; border-radius: 50%;
    display: flex; align-items: center; justify-content: center;
  }
  .value-badge svg { width: 44px; height: 44px; }
  .teamwork .value-band, .teamwork .value-badge { background: var(--teamwork); }
  .honesty .value-band, .honesty .value-badge { background: var(--honesty); }
  .accountability .value-band, .accountability .value-badge { background: var(--accountability); }
  .excellence .value-band, .excellence .value-badge { background: var(--excellence); }
  .family .value-band, .family .value-badge { background: var(--family); }
  .motto {
    position: absolute; left: 0; width: 800px; top: 1132px; text-align: center;
    font-weight: 700; font-style: italic; font-size: 22px; color: var(--ink);
  }
</style>
</head>
<body>
<main class="poster">
  <header class="brand">
    <div class="brand-name">BRIGHTWELL</div>
    <div class="brand-tagline">CONNECT. DELIVER. DAILY.</div>
  </header>

  <h1 class="title">VALUES</h1>

  <div class="presenter" role="img" aria-label="Illustration of a smiling woman in an orange shirt and navy trousers pointing toward the values list"></div>

  <section class="value teamwork">
    <div class="value-card" style="left:98px;top:291px;width:241px;height:175px;">Acknowledging strengths-weaknesses,<br>Compromise,<br>Active listening,<br>Punctuality,<br>Open to Feedback,<br>Mutual Respect</div>
    <div class="value-band" style="left:102px;top:256px;width:237px;">TEAMWORK</div>
    <div class="value-badge" style="left:40px;top:238px;">
      <svg viewBox="0 0 44 44" fill="#fff"><circle cx="22" cy="13" r="6"/><circle cx="10" cy="16" r="4.5"/><circle cx="34" cy="16" r="4.5"/><path d="M12 34c0-7 4-12 10-12s10 5 10 12z"/><path d="M2 33c0-5 3-9 8-9 2 0 3 .5 4 1-2 2-3.5 5-3.5 8z"/><path d="M42 33c0-5-3-9-8-9-2 0-3 .5-4 1 2 2 3.5 5 3.5 8z"/></svg>
    </div>
  </section>

  <section class="value honesty">
    <div class="value-card" style="left:98px;top:540px;width:253px;height:150px;">Integrity,<br>Pschological Safety,<br>Vulnerability,<br>Dependable,<br>Ethical,<br>Truthful</div>
    <div class="value-band" style="left:102px;top:505px;width:249px;">HONESTY</div>
    <div class="value-badge" style="left:40px;top:488px;">
      <svg viewBox="0 0 44 44" fill="none" stroke="#fff" stroke-width="5" stroke-linecap="round" stroke-linejoin="round"><path d="M7 23l9 9L37 10"/></svg>
    </div>
  </section>

  <section class="value accountability">
    <div class="value-card" style="left:98px;top:765px;width:253px;height:110px;">Integrity<br>Trust<br>Self-Discipline<br>Tranparency</div>
    <div class="value-band" style="left:102px;top:731px;width:249px;">ACCOUNTABILITY</div>
    <div class="value-badge" style="left:40px;top:712px;">
      <svg viewBox="0 0 44 44" fill="#fff"><path d="M2 17l8-6 6 3 6-3 6 1 6-3 8 6-6 10-10 9-4-3-3 2-4-3-2 1-5-5z"/><path d="M16 14l-4 6 3 2 6-5" fill="none" stroke="#f37021" stroke-width="1.6"/></svg>
    </div>
  </section>

  <section class="value excellence">
    <div class="value-card" style="left:97px;top:955px;width:255px;height:150px;padding-left:16px;">Consistent Quality,<br>Continuous Improvement,<br>Attention to Detail,<br>Accepting Challenges,<br>Service to others<br>(internally &amp; externally)</div>
    <div class="value-band" style="left:102px;top:921px;width:250px;">EXCELLENCE</div>
    <div class="value-badge" style="left:40px;top:904px;">
      <svg viewBox="0 0 44 44" fill="#fff"><path d="M22 3l5.6 12.4 13.4 1.4-10 9.1 2.9 13.3L22 32.4 10.1 39.2 13 25.9 3 16.8l13.4-1.4z"/></svg>
    </div>
  </section>

  <section class="value family">
    <div class="value-card" style="left:469px;top:962px;width:253px;height:135px;">Acceptance,<br>Compassion,<br>Being there for<br>each other,<br>Celebrating Successes</div>
    <div class="value-band" style="left:469px;top:926px;width:253px;padding-left:18px;">FAMILY</div>
    <div class="value-badge" style="left:409px;top:909px;">
      <svg viewBox="0 0 44 44" fill="#fff"><path d="M22 39S4 28 4 15.5C4 9.5 8.5 5 14 5c3.6 0 6.4 2 8 5 1.6-3 4.4-5 8-5 5.5 0 10 4.5 10 10.5C40 28 22 39 22 39z"/></svg>
    </div>
  </section>

  <p class="motto">Guided by Values. Driven by Purpose.</p>
</main>
</body>
</html>
```